Icons for web and velmoKIT app

Following our velmoKIT project, we need a set of icons for the app and web service users, versions in English and Spanish. In the enclosed documentation please find the icons that we need, criteria and texts. We need these icons to be consistent with the colors of the velmoKIT logo, so we plase it as well

Target Market(s)

Busy people

Industry/Entity Type

Business Service

Font styles to use
Sans Serif

Colors
abd036

Requirements
Must have
• THE SET OF NINE ICONS IN ENGLISH AND SPANISH
Nice to have
• OTHER WEB NAVIGATION ITEMS

```html
<!DOCTYPE html>
<html lang="es">
<head>
<meta charset="utf-8">
<title>velmoKIT – app home</title>
<link rel="stylesheet" href="https://fonts.googleapis.com/css2?family=Open+Sans:wght@400;600;700;800&display=swap">
<style>
  :root {
    --page-bg: #ffffff;
    --screen-top: #ffffff;
    --screen-bottom: #a9aaac;
    --brand-green: #2e9612;
    --btn-green-light: #35a016;
    --btn-green-dark: #1d790b;
    --rule-grey: #8a8a8a;
    --ink: #141414;
    --white: #ffffff;
  }
  html, body {
    margin: 0;
    padding: 0;
    width: 848px;
    height: 1200px;
    overflow: hidden;
    background: var(--page-bg);
    font-family: "Open Sans", Arial, sans-serif;
  }
  .app-screen {
    position: absolute;
    left: 85px;
    top: 0;
    width: 678px;
    height: 1200px;
    background: linear-gradient(165deg, var(--screen-top) 0%, var(--screen-top) 45%, #e9eaeb 70%, var(--screen-bottom) 100%);
    overflow: hidden;
  }
  .brand-name {
    position: absolute;
    left: 60px;
    top: 52px;
    width: 528px;
    margin: 0;
    text-align: center;
    font-size: 100px;
    font-weight: 800;
    line-height: 120px;
    letter-spacing: -2px;
    color: var(--brand-green);
  }
  .brand-rule {
    position: absolute;
    left: 60px;
    top: 207px;
    width: 528px;
    height: 10px;
    background: var(--rule-grey);
  }
  .prompt {
    position: absolute;
    left: 0;
    top: 278px;
    width: 100%;
    margin: 0;
    text-align: center;
    font-size: 35px;
    font-weight: 400;
    color: var(--ink);
  }
  .action-list {
    position: absolute;
    left: 234px;
    top: 390px;
    width: 204px;
    margin: 0;
    padding: 0;
    list-style: none;
  }
  .action-btn {
    position: relative;
    width: 204px;
    height: 204px;
    margin-bottom: 18px;
    border-radius: 12px;
    background: linear-gradient(160deg, var(--btn-green-light), var(--btn-green-dark));
    color: var(--white);
  }
  .action-btn svg {
    position: absolute;
    left: 52px;
    top: 28px;
    width: 100px;
    height: 100px;
  }
  .action-label {
    position: absolute;
    left: 0;
    bottom: 22px;
    width: 100%;
    text-align: center;
    font-size: 23px;
    font-weight: 600;
    letter-spacing: 0.3px;
  }
  .delivery-icon {
    position: absolute;
    left: 545px;
    top: 1082px;
    width: 74px;
    height: 54px;
  }
</style>
</head>
<body>
  <main class="app-screen">
    <h1 class="brand-name">velmoKIT</h1>
    <div class="brand-rule"></div>
    <p class="prompt">¿EN QUE PUEDO AYUDARTE?</p>

    <ul class="action-list">
      <li class="action-btn">
        <svg viewBox="0 0 100 100" aria-hidden="true">
          <circle cx="40" cy="20" r="16" fill="none" stroke="#fff" stroke-width="6"/>
          <path d="M33 22 a7 7 0 0 1 14 0 V50 l20 8 a8 8 0 0 1 6 9 L70 92 H30 L12 72 a6 6 0 0 1 8 -8 L33 72 Z" fill="#fff"/>
        </svg>
        <span class="action-label">SERVICES</span>
      </li>
      <li class="action-btn">
        <svg viewBox="0 0 100 100" aria-hidden="true">
          <path d="M50 10 L76 24 L76 52 L50 66 L24 52 L24 24 Z" fill="none" stroke="#fff" stroke-width="7" stroke-linejoin="round"/>
          <path d="M24 24 L50 38 L76 24 M50 38 V66" fill="none" stroke="#fff" stroke-width="7" stroke-linejoin="round"/>
          <path d="M8 52 L14 84 L30 96 L38 96 L36 80 L26 66 Z M92 52 L86 84 L70 96 L62 96 L64 80 L74 66 Z" fill="#fff"/>
        </svg>
        <span class="action-label">RECOGER</span>
      </li>
      <li class="action-btn">
        <svg viewBox="0 0 100 100" aria-hidden="true">
          <rect x="6" y="6" width="88" height="88" rx="10" fill="#fff"/>
          <rect x="18" y="16" width="64" height="50" fill="#248410"/>
          <path d="M42 22 H58 V40 H70 L50 62 L30 40 H42 Z" fill="#fff"/>
        </svg>
        <span class="action-label">RECIBIR</span>
      </li>
    </ul>

    <svg class="delivery-icon" viewBox="0 0 74 54" role="img" aria-label="Reparto">
      <rect x="2" y="2" width="44" height="38" rx="3" fill="#fff"/>
      <path d="M48 14 H62 L72 28 V40 H48 Z" fill="#fff"/>
      <path d="M52 18 H60 L66 27 H52 Z" fill="#b5b6b8"/>
      <circle cx="16" cy="44" r="8" fill="#fff" stroke="#b5b6b8" stroke-width="3"/>
      <circle cx="58" cy="44" r="8" fill="#fff" stroke="#b5b6b8" stroke-width="3"/>
    </svg>
  </main>
</body>
</html>
```